Pel'k Marrowind Travel

We need a sleek, professional, inviting card to elicit global travel for the experienced and professional traveler. Royal blue, black and silver. (perhaps the wording could be silver with black shadow?-get creative) Maybe a watermark on the front and the full raised logo on the back.
We want a stylish and modern card, but professional.

```html
<!DOCTYPE html>
<html lang="en">
<head>
<meta charset="utf-8">
<title>Pel'k Marrowind Travel – Business Card</title>
<link rel="stylesheet" href="https://fonts.googleapis.com/css2?family=Montserrat:wght@400;500;600;700&display=swap">
<style>
  :root {
    --sky: #29a8e0;
    --sky-deep: #1f95cc;
    --leaf: #8dc63f;
    --ink: #1f1f1f;
    --paper: #ffffff;
    --stage: #b9b9b9;
    --ghost: rgba(0, 0, 0, 0.045);
  }
  * { box-sizing: border-box; margin: 0; padding: 0; }
  html, body {
    width: 1200px; height: 900px; overflow: hidden;
    background: var(--stage);
    font-family: "Montserrat", sans-serif;
  }
  .canvas {
    position: relative; width: 1200px; height: 900px;
    display: flex; flex-direction: column; align-items: center; justify-content: center; gap: 44px;
  }
  .card {
    position: relative; width: 630px; height: 360px;
    border-radius: 34px; overflow: hidden;
    box-shadow: 0 10px 22px rgba(0,0,0,0.28);
  }
  /* Front */
  .card--front { background: var(--sky); }
  .front__sky {
    position: absolute; right: 30px; top: 24px; width: 260px; height: 120px;
    border-radius: 60px;
    background: radial-gradient(ellipse at center, rgba(0,60,110,0.14), rgba(0,60,110,0) 70%);
  }
  .front__ghost {
    position: absolute; left: 90px; top: 60px; width: 300px; height: 300px;
    border-radius: 50%; background: rgba(255,255,255,0.06);
  }
  .wordmark {
    position: absolute; left: 50%; top: 50%; transform: translate(-50%, -50%);
    text-align: center; white-space: nowrap;
  }
  .wordmark__name {
    font-weight: 600; font-size: 32px; letter-spacing: 2px; text-transform: uppercase;
  }
  .wordmark__rule {
    height: 2px; margin-top: 10px;
  }
  .card--front .wordmark__name { color: var(--paper); }
  .card--front .wordmark__rule { background: var(--paper); }

  /* Back */
  .card--back { background: var(--paper); }
  .back__ghost {
    position: absolute; right: -40px; top: -60px; width: 330px; height: 330px;
    border-radius: 50%; background: var(--ghost);
  }
  .back__brand {
    position: absolute; left: 48px; top: 52px;
  }
  .back__brand .wordmark__name { color: var(--sky); font-size: 26px; letter-spacing: 1.5px; font-weight: 600; text-transform: uppercase; }
  .back__brand .wordmark__rule { background: var(--leaf); width: 100%; margin-top: 8px; }

  .person { position: absolute; left: 48px; top: 140px; }
  .person__name { color: var(--sky); font-weight: 700; font-size: 24px; letter-spacing: 1px; text-transform: uppercase; }
  .person__role { color: var(--leaf); font-weight: 500; font-size: 14px; letter-spacing: 1px; text-transform: uppercase; margin-top: 2px; }

  .contacts { position: absolute; left: 48px; top: 210px; list-style: none; }
  .contacts li {
    display: flex; align-items: center; gap: 10px;
    font-size: 15px; color: var(--ink); line-height: 26px;
  }
  .contacts .hl { color: var(--sky); }
  .contacts svg { width: 18px; height: 18px; flex: none; }

  .address {
    position: absolute; right: 44px; bottom: 100px; text-align: right;
    font-size: 15px; color: var(--ink); line-height: 22px;
  }
</style>
</head>
<body>
<main class="canvas">

  <section class="card card--front" aria-label="Card front">
    <div class="front__sky" role="img" aria-label="Faint aircraft silhouettes in the sky"></div>
    <div class="front__ghost"></div>
    <div class="wordmark">
      <div class="wordmark__name">Pel'k Marrowind Travel</div>
      <div class="wordmark__rule"></div>
    </div>
  </section>

  <section class="card card--back" aria-label="Card back">
    <div class="back__ghost"></div>

    <div class="back__brand">
      <div class="wordmark__name">Pel'k Marrowind Travel</div>
      <div class="wordmark__rule"></div>
    </div>

    <div class="person">
      <div class="person__name">Dorian Vell</div>
      <div class="person__role">Managing Director</div>
    </div>

    <ul class="contacts">
      <li>
        <svg viewBox="0 0 18 18"><rect width="18" height="18" rx="4" fill="var(--sky)"/><path d="M5 4.5l2 0 1 2.5-1.3 1a6 6 0 0 0 2.8 2.8l1-1.3 2.5 1 0 2c0 .6-.5 1-1 1A8.5 8.5 0 0 1 4 5.5c0-.6.4-1 1-1z" fill="#fff"/></svg>
        044-987 654 321
      </li>
      <li>
        <svg viewBox="0 0 18 18"><rect width="18" height="18" rx="4" fill="var(--sky)"/><rect x="6" y="3.5" width="6" height="11" rx="1.2" fill="none" stroke="#fff" stroke-width="1.4"/></svg>
        044-987 654 321
      </li>
      <li>
        <svg viewBox="0 0 18 18"><rect width="18" height="18" rx="4" fill="var(--sky)"/><rect x="3.5" y="5.5" width="11" height="7" fill="none" stroke="#fff" stroke-width="1.3"/><path d="M3.5 5.5l5.5 4 5.5-4" fill="none" stroke="#fff" stroke-width="1.3"/></svg>
        hello@marrowind.com
      </li>
      <li>
        <svg viewBox="0 0 18 18"><rect width="18" height="18" rx="4" fill="var(--sky)"/><circle cx="9" cy="9" r="5" fill="none" stroke="#fff" stroke-width="1.2"/><path d="M4 9h10M9 4c-2.4 3-2.4 7 0 10M9 4c2.4 3 2.4 7 0 10" fill="none" stroke="#fff" stroke-width="1"/></svg>
        <span>www.<span class="hl">marrowind</span>.com</span>
      </li>
    </ul>

    <address class="address" style="font-style:normal">
      421, Address line goes here<br>
      45452, Country Name
    </address>
  </section>

</main>
</body>
</html>
```